Business Card for Luxury Hospitality Industry Career Seeker

Need something Simple, Punctual, and Elegant.

Project goal is to update phone number, layout, and wording

I look forward to working with you to create a business card I can give to managers and employers in the Luxury Hospitality industry. I want to advance a career in this industry handing out cards to managers and directors on my way up.
Updates

Updated graphics preferences in brief - would like my name flanked by small Lion, Compass, & Rope and have the Halworth 5 Star logo on the back Added Saturday, January 14, 2017

Updated Brief:-Some wording has been removed-Card Front should be more simple and tidy now-Card Back word choice & flow is improved Added Sunday, January 15, 2017

Target Market(s)

Luxury Hospitality Industry Employers and Managers

Industry/Entity Type

Hospitality

Contact Information for Business Card

(Card Front)
Corbin T. Pellman (flanked by small Lion, Compass & Rope graphic)
Luxury Hospitality
555-317-8846
ridgefellow@mailvessel.example
netroster.example/in/corbin-pellman-vet-civ
My Experience = Our Success

(Card Back)
Graphic of: Halworth 5 Star logo and maybe QTR 5 Diamond Logo too
8 years military supply, logistics, & administrative experience
2 years intensive recruiting, marketing, and sales expertise
Adept problem solving, planning and management skills
5 Star, 5 Daimond, Luxury Hotels & Hospitality Rooms & Revenue

Requirements
Must have
• Name
• Phone Number
• Email Address
• Net Roster Address
• Slogan (My Experience = Our Success)
• Graphic on back: Halworth 5 Star logo
• Qualification Remarks
• Catchy logo
Nice to have
• Background that makes a viewer think Luxury Hospitality Experience and/or World Experience
• Color combinations I've seen & liked are black & yellow, black & white, and blue & white

```html
<!DOCTYPE html>
<html lang="en">
<head>
<meta charset="utf-8">
<title>Corbin T. Pellman — Luxury Hospitality Business Card</title>
<link href="https://fonts.googleapis.com/css2?family=Cinzel:wght@400;500&display=swap" rel="stylesheet">
<style>
  :root {
    --card-blue: #0a74b4;
    --ink-black: #050505;
    --band-black: #141414;
    --paper-white: #ffffff;
    --accent-blue: #1a86c8;
    --stage: #d9dadc;
  }
  * { box-sizing: border-box; margin: 0; padding: 0; }
  html, body {
    width: 1200px; height: 1200px; overflow: hidden;
    background: var(--stage);
    font-family: "Cinzel", "Times New Roman", serif;
  }
  .sheet {
    width: 1200px; height: 1200px;
    display: flex; flex-direction: column; align-items: center; justify-content: center;
    gap: 56px;
  }
  .card {
    width: 900px; height: 514px; position: relative; overflow: hidden;
    color: var(--paper-white);
    box-shadow: 0 6px 18px rgba(0,0,0,.18);
  }

  /* Front */
  .card--front { background: var(--card-blue); }
  .brand {
    position: absolute; left: 70px; top: 40px;
    display: flex; align-items: center; gap: 30px;
  }
  .brand__emblem { width: 120px; height: 120px; flex: none; }
  .brand__title { line-height: 1; }
  .brand__luxury { font-size: 84px; letter-spacing: 2px; }
  .brand__hospitality { font-size: 46px; letter-spacing: 1px; margin-top: 6px; padding-left: 48px; }
  .brand__tagline { font-size: 15px; letter-spacing: 1px; margin-top: 8px; padding-left: 90px; }
  .name-band {
    position: absolute; left: 0; right: 0; top: 222px; height: 64px;
    background: var(--band-black);
    display: flex; align-items: center; padding-left: 70px;
    font-size: 36px; letter-spacing: 1.5px;
  }
  .contact { position: absolute; left: 120px; top: 318px; }
  .contact__phone { font-size: 50px; letter-spacing: 3px; }
  .contact__line { font-size: 20px; letter-spacing: .8px; margin-top: 12px; }
  .contact__line + .contact__line { margin-top: 6px; }

  /* Back */
  .card--back { background: var(--ink-black); padding: 44px 60px; }
  .quals {
    display: grid; grid-template-columns: 1fr 1fr; column-gap: 50px; row-gap: 30px;
  }
  .qual__lead { color: var(--accent-blue); font-size: 34px; line-height: 1.05; letter-spacing: 1px; }
  .qual__text { font-size: 21px; line-height: 1.18; letter-spacing: .6px; }
  .awards {
    position: absolute; right: 60px; bottom: 44px;
    display: flex; align-items: center; gap: 34px;
  }
  .award-badge { width: 84px; height: 84px; }
  .award-name { display: flex; align-items: center; gap: 10px; font-size: 38px; }
  .award-name__mark { width: 12px; height: 12px; background: var(--paper-white); }
</style>
</head>
<body>
<main class="sheet">

  <section class="card card--front" aria-label="Card front">
    <div class="brand">
      <svg class="brand__emblem" viewBox="0 0 120 120" role="img" aria-label="Lion, Compass & Rope emblem">
        <circle cx="60" cy="60" r="56" fill="#e9eef2"/>
      </svg>
      <div class="brand__title">
        <div class="brand__luxury">LUXURY</div>
        <div class="brand__hospitality">HOSPITALITY</div>
        <div class="brand__tagline">MY EXPERIENCE = OUR SUCCESS</div>
      </div>
    </div>
    <div class="name-band">CORBIN T. PELLMAN</div>
    <div class="contact">
      <div class="contact__phone">555-317-8846</div>
      <div class="contact__line">RIDGEFELLOW@MAILVESSEL.EXAMPLE</div>
      <div class="contact__line">NETROSTER.EXAMPLE/IN/CORBIN-PELLMAN-VET-CIV</div>
    </div>
  </section>

  <section class="card card--back" aria-label="Card back">
    <div class="quals">
      <div class="qual">
        <div class="qual__lead">8 YEARS</div>
        <div class="qual__text">MILITARY SUPPLY,<br>LOGISTICS, &amp;<br>ADMINISTRATIVE<br>EXPERIENCE</div>
      </div>
      <div class="qual">
        <div class="qual__lead">2 YEARS</div>
        <div class="qual__text">INTENSIVE RECRUITING,<br>MARKETING, AND SALES<br>EXPERTISE</div>
      </div>
      <div class="qual">
        <div class="qual__text">ADEPT PROBLEM<br>SOLVING, PLANNING AND<br>MANAGEMENT SKILLS</div>
      </div>
      <div class="qual">
        <div class="qual__lead">5 STAR,<br>5 DAIMOND,</div>
        <div class="qual__text">LUXURY HOTELS<br>&amp; HOSPITALITY<br>ROOMS &amp; REVENUE</div>
      </div>
    </div>
    <div class="awards">
      <svg class="award-badge" viewBox="0 0 84 84" role="img" aria-label="QTR 5 Diamond award badge">
        <circle cx="42" cy="42" r="38" fill="none" stroke="#ffffff" stroke-width="3"/>
      </svg>
      <div class="award-name"><span class="award-name__mark"></span>HALWORTH</div>
    </div>
  </section>

</main>
</body>
</html>
```